Rivet Athletic Supply Inc.

Need to create a website that is informational and has the ability to sell goods and services. Such as a custom t shirt designer where the user can upload and image to be displayed on the garmet. The sports we specialize in are basketball, football, and baseball.

Would like like:
Home Page
Locker Room Page:
Custom Uniforms Page
Custom Shirt Creator
Brands
About

Competitor websites are
lornfieldsportsco.example
qtv.example
wmdgear.example

```html
<!DOCTYPE html>
<html lang="en">
<head>
<meta charset="utf-8">
<title>Rivet Athletic Supply – Home</title>
<link href="https://fonts.googleapis.com/css2?family=Questrial&display=swap" rel="stylesheet">
<style>
:root{
  --blue:#2a5fae;
  --blue-dark:#1f4c92;
  --red:#d0403f;
  --red-soft:#c9403e;
  --ink:#1d1d1f;
  --text:#444;
  --muted:#9a9a9a;
  --light:#f4f4f4;
  --white:#fff;
}
*{box-sizing:border-box;margin:0;padding:0}
html,body{width:1200px;height:3131px;overflow:hidden}
body{font-family:"Questrial",sans-serif;color:var(--ink);background:var(--white);position:relative}
.abs{position:absolute}
a{color:inherit;text-decoration:none}

/* header */
.site-header{position:absolute;left:0;top:0;width:1200px;height:72px;background:var(--white);border-bottom:1px solid #e6e6e6}
.brand{position:absolute;left:145px;top:18px;display:flex;align-items:center;gap:8px;font-size:20px;color:var(--blue);font-weight:400;line-height:1}
.brand-dot{width:30px;height:30px;border-radius:50%;background:var(--red)}
.main-nav{position:absolute;left:407px;top:29px;display:flex;gap:24px;font-size:14px;color:#333}
.main-nav .active{color:var(--red)}
.cart{position:absolute;left:1027px;top:27px}
.cart-count{position:absolute;left:1042px;top:26px;width:12px;height:12px;border-radius:50%;background:var(--red);color:#fff;font-size:8px;text-align:center;line-height:12px}

/* hero */
.hero{position:absolute;left:0;top:72px;width:1200px;height:560px;background:linear-gradient(180deg,#c8cacb 0%,#a9adae 45%,#5f6b47 70%,#4b5a33 100%)}
.hero-photo{position:absolute;left:560px;top:0;width:640px;height:560px;background:radial-gradient(ellipse at 55% 45%,#3a3535 0%,#5a5352 45%,rgba(120,118,115,0) 75%)}
.hero-title{position:absolute;left:140px;top:124px;font-size:56px;line-height:72px;color:var(--ink)}
.hero-title .b{color:var(--blue)}
.hero-title .r{color:var(--red)}
.hero-sub{position:absolute;left:144px;top:276px;font-size:17px;line-height:29px;color:#1c1c1c}
.btn-outline-red{position:absolute;left:144px;top:371px;width:240px;height:48px;background:var(--red);border:2px solid #fff;color:#fff;font-size:16px;text-align:center;line-height:44px}
.scroll-down{position:absolute;left:0;width:1200px;top:502px;text-align:center;color:#fff;font-size:11px;letter-spacing:1.5px}

/* sections */
.section-title{position:absolute;left:0;width:1200px;text-align:center;font-size:36px;letter-spacing:.5px;color:var(--ink)}
.rule{position:absolute;left:564px;width:72px;height:3px;background:var(--blue)}

.sport-card{position:absolute;top:795px;width:296px;height:319px;color:#fff;text-align:center}
.sport-card.blue{background:linear-gradient(180deg,#3b5677 0%,#22467e 60%,#1d4b95 100%)}
.sport-card.red{background:rgba(208,64,63,.93)}
.sport-card .label{position:absolute;left:0;width:100%;font-size:17px}
.sport-card p{position:absolute;left:20px;width:256px;top:142px;font-size:13px;line-height:23px}
.sport-card .more{position:absolute;left:0;width:100%;top:255px;font-size:14px;text-decoration:underline}
.sport-icon{position:absolute;left:124px;width:48px;height:48px}

.product{position:absolute;top:1287px;width:216px;height:240px;text-align:center}
.product.featured{background:#fff;box-shadow:0 3px 12px rgba(0,0,0,.14)}
.product .shot{position:absolute;left:48px;top:20px;width:120px;height:130px;border-radius:6px}
.product .name{position:absolute;left:0;width:100%;top:180px;font-size:13px;color:#333}
.product .price{position:absolute;left:0;width:100%;top:208px;font-size:13px}
.price s{color:var(--muted);margin-right:8px}
.price span{color:var(--blue)}
.featured .price span{color:var(--red)}
.arrow{position:absolute;width:14px;height:14px}

.btn-red{position:absolute;background:var(--red);color:#fff;font-size:16px;text-align:center}

.cta{position:absolute;left:0;top:1708px;width:1200px;height:260px;background:linear-gradient(90deg,#cf4241,#c83c3b 60%,#c84241)}
.cta h2{position:absolute;left:0;width:1200px;top:56px;text-align:center;color:#fff;font-size:48px;font-weight:400}
.cta .btn{position:absolute;left:492px;top:148px;width:216px;height:44px;border:2px solid #fff;color:#fff;font-size:16px;text-align:center;line-height:40px}

.about-frame{position:absolute;left:125px;top:2079px;width:425px;height:405px;background:var(--blue)}
.about-photo{position:absolute;left:143px;top:2049px;width:438px;height:418px;background:linear-gradient(160deg,#8fa8c4 0%,#c24a42 45%,#d84a3f 70%,#6f8b56 100%)}
.about-title{position:absolute;left:643px;top:2094px;font-size:36px}
.about-rule{position:absolute;left:643px;top:2145px;width:72px;height:3px;background:var(--blue)}
.about-text{position:absolute;left:643px;width:413px;font-size:13px;line-height:23px;color:#555;text-align:justify}

.brands{position:absolute;left:0;top:2565px;width:1200px;height:261px;background:var(--light)}
.brand-box{position:absolute;top:126px;width:172px;height:72px;background:#fff;display:flex;align-items:center;justify-content:center;gap:8px;font-size:21px;color:#111}
.brand-box i{display:block;width:22px;height:22px;border-radius:50%;background:#111}

.site-footer{position:absolute;left:0;top:2826px;width:1200px;height:305px;background:var(--blue);color:#fff}
.foot-brand{position:absolute;left:145px;top:96px;display:flex;align-items:center;gap:8px;font-size:20px}
.foot-brand .brand-dot{background:var(--red)}
.socials{position:absolute;left:187px;top:154px;display:flex;gap:11px}
.socials span{width:28px;height:28px;border-radius:50%;border:1.5px solid #fff}
.socials span.on{background:var(--red)}
.foot-col{position:absolute;top:52px}
.foot-col h4{font-weight:400;font-size:17px;margin-bottom:14px}
.foot-col li{list-style:none;font-size:13px;line-height:24px}
.contact li{display:flex;gap:14px;margin-bottom:16px;line-height:23px}
.foot-rule{position:absolute;left:145px;top:260px;width:911px;height:1px;background:rgba(255,255,255,.5)}
.copyright{position:absolute;left:0;width:1200px;top:280px;text-align:center;font-size:13px}
</style>
</head>
<body>

<header class="site-header">
  <div class="brand"><span class="brand-dot"></span>Rivet Athletic Supply</div>
  <nav class="main-nav">
    <a class="active">Home</a><a>About Us</a><a>Locker Room</a><a>Custom Uniforms</a><a>Custom Shirt Creator</a><a>Brands</a>
  </nav>
  <svg class="cart" width="22" height="20" viewBox="0 0 22 20" fill="none" stroke="#2a5fae" stroke-width="1.4"><path d="M1 2h3l3 11h11l2-8H6"/><circle cx="9" cy="17" r="1.5"/><circle cx="16" cy="17" r="1.5"/></svg>
  <span class="cart-count">0</span>
</header>

<section class="hero">
  <div class="hero-photo" role="img" aria-label="Team of players in black kits celebrating on a grass field"></div>
  <h1 class="hero-title" style="font-weight:400"><span class="b">Built</span> For Teams.<br><span class="r">Designed</span> To Win.</h1>
  <p class="hero-sub">Custom Uniforms, Spirit Wear, and Sporting Goods<br>For Basketball, Football, And Baseball.</p>
  <a class="btn-outline-red">DESIGN YOUR UNIFORM</a>
  <div class="scroll-down">SCROLL DOWN<br>
    <svg width="12" height="8" viewBox="0 0 12 8" style="margin-top:6px"><path d="M1 1l5 5 5-5" stroke="#fff" stroke-width="1.5" fill="none"/></svg>
  </div>
</section>

<h2 class="section-title" style="top:700px;font-weight:400">YOUR TEAM SPORTS SPECIALISTS</h2>
<div class="rule" style="top:761px"></div>

<article class="sport-card blue" style="left:145px" role="img" aria-label="Basketball player dunking at the hoop">
  <svg class="sport-icon" style="top:212px" viewBox="0 0 48 48" fill="none" stroke="#fff" stroke-width="2"><circle cx="24" cy="24" r="22"/><path d="M2 24h44M24 2v44M8 9c8 7 8 23 0 30M40 9c-8 7-8 23 0 30"/></svg>
  <div class="label" style="top:278px">BASKETBALL</div>
</article>
<article class="sport-card red" style="left:453px">
  <svg class="sport-icon" style="top:46px" viewBox="0 0 48 48" fill="none" stroke="#fff" stroke-width="2"><circle cx="24" cy="24" r="22"/><path d="M24 15l8 6-3 10H19l-3-10zM24 15V4M32 21l11-3M29 31l6 10M19 31l-6 10M16 21L5 18"/></svg>
  <div class="label" style="top:114px">FOOTBALL</div>
  <p>Lorem ipsum dolor sit amet, consectetur adipiscing elit, sed do eiusmod tempor incididunt ut labore et dolore magna aliqu enim ad minim veniam,</p>
  <a class="more">LEARN MORE</a>
</article>
<article class="sport-card blue" style="left:760px" role="img" aria-label="Baseball batter swinging in a stadium">
  <svg class="sport-icon" style="top:212px" viewBox="0 0 48 48" fill="none" stroke="#fff" stroke-width="2"><circle cx="24" cy="24" r="22"/><path d="M14 5c6 10 6 28 0 38M34 5c-6 10-6 28 0 38"/></svg>
  <div class="label" style="top:278px">BASEBALL</div>
</article>

<h2 class="section-title" style="top:1183px;font-weight:400">UNIFORMS THAT SET THE STANDARD</h2>
<div class="rule" style="top:1242px"></div>

<svg class="arrow" style="left:98px;top:1401px" viewBox="0 0 14 14"><path d="M9 1L3 7l6 6" stroke="#222" stroke-width="1.6" fill="none"/></svg>
<svg class="arrow" style="left:1086px;top:1401px" viewBox="0 0 14 14"><path d="M5 1l6 6-6 6" stroke="#222" stroke-width="1.6" fill="none"/></svg>

<div class="product" style="left:144px">
  <div class="shot" role="img" aria-label="Black and orange jersey" style="background:linear-gradient(160deg,#3a3a3a,#1c1c1c 60%,#d8772a)"></div>
  <div class="name">Lorem ipsum dolor sit</div>
  <div class="price"><s>$50.00</s><span>$39.95</span></div>
</div>
<div class="product featured" style="left:376px">
  <div class="shot" role="img" aria-label="Red athletic shorts" style="background:linear-gradient(180deg,#e4321f,#c72414)"></div>
  <svg class="abs" style="left:179px;top:12px" width="22" height="20" viewBox="0 0 22 20" fill="none" stroke="#d0403f" stroke-width="1.3"><path d="M1 2h3l3 11h11l2-8H6"/><circle cx="9" cy="17" r="1.5"/><circle cx="16" cy="17" r="1.5"/></svg>
  <svg class="abs" style="left:182px;top:47px" width="16" height="16" viewBox="0 0 16 16" fill="none" stroke="#d0403f" stroke-width="1.2"><path d="M1 5V1h4M11 1h4v4M15 11v4h-4M5 15H1v-4M1 1l5 5M15 1l-5 5M15 15l-5-5M1 15l5-5"/></svg>
  <div class="name">Lorem ipsum dolor sit</div>
  <div class="price"><s>$50.00</s><span>$39.95</span></div>
</div>
<div class="product" style="left:607px">
  <div class="shot" role="img" aria-label="Blue athletic shorts with red side stripe" style="background:linear-gradient(180deg,#2a86e6,#1b6cd0)"></div>
  <div class="name">Lorem ipsum dolor sit</div>
  <div class="price"><s>$50.00</s><span>$39.95</span></div>
</div>
<div class="product" style="left:838px">
  <div class="shot" role="img" aria-label="Black and white striped jersey" style="background:linear-gradient(90deg,#222,#eee,#222,#eee,#222)"></div>
  <div class="name">Lorem ipsum dolor sit</div>
  <div class="price"><s>$50.00</s><span>$39.95</span></div>
</div>

<a class="btn-red" style="left:532px;top:1583px;width:136px;height:44px;line-height:44px">VIEW ALL</a>

<section class="cta" role="img" aria-label="Red-tinted crowd of cheering fans">
  <h2>READY TO GEAR UP YOUR TEAM?</h2>
  <a class="btn">START YOUR DESIGN</a>
</section>

<div class="about-frame"></div>
<div class="about-photo" role="img" aria-label="Players in red and white kits celebrating together"></div>
<h2 class="about-title" style="font-weight:400">ABOUT RIVET ATHLETIC</h2>
<div class="about-rule"></div>
<p class="about-text" style="top:2169px">Lorem ipsum dolor sit amet, consectetur adipiscing elit, sed do eius-mod tempor incididunt ut labore et dolore magna aliqua. Ut enim ad minim veniam, quis nostrud exercitation ullamco</p>
<p class="about-text" style="top:2247px">Duis aute irure dolor in reprehenderit in voluptate velit esse cillum dolore eu fugiat nulla pariatur. Excepteur sint occaecat cupidatat non proident, sunt in culpa qui officia deserunt mollit anim id est laborum totam rem aperiam, eaque ipsa quae</p>
<a class="btn-red" style="left:643px;top:2374px;width:145px;height:44px;line-height:44px">READ MORE</a>

<section class="brands">
  <h2 class="section-title" style="top:48px;font-weight:400">OUR BRANDS</h2>
  <svg class="arrow" style="left:98px;top:155px" viewBox="0 0 14 14"><path d="M9 1L3 7l6 6" stroke="#222" stroke-width="1.6" fill="none"/></svg>
  <svg class="arrow" style="left:1086px;top:155px" viewBox="0 0 14 14"><path d="M5 1l6 6-6 6" stroke="#222" stroke-width="1.6" fill="none"/></svg>
  <div class="brand-box" style="left:145px"><i></i>Kestrel</div>
  <div class="brand-box" style="left:330px"><i></i>Harbor</div>
  <div class="brand-box" style="left:514px;letter-spacing:3px;font-size:18px"><i></i>NORTHLINE</div>
  <div class="brand-box" style="left:698px"><i></i>Vantage</div>
  <div class="brand-box" style="left:883px"><i></i>Summit</div>
</section>

<footer class="site-footer">
  <div class="foot-brand"><span class="brand-dot"></span>Rivet Athletic Supply</div>
  <div class="socials" aria-label="Social links"><span></span><span class="on"></span><span></span><span></span></div>
  <div class="foot-col" style="left:428px">
    <h4>Information</h4>
    <ul><li>Home</li><li>About Us</li><li>Locker Room</li><li>Custom Uniforms</li><li>Custom Shirt Creator</li><li>Brands</li></ul>
  </div>
  <div class="foot-col" style="left:629px">
    <h4>Quick Links</h4>
    <ul><li>Terms &amp; Conditions</li><li>Privacy Policy</li><li>Sitemap</li><li>Contact</li></ul>
  </div>
  <div class="foot-col contact" style="left:821px">
    <h4>Contact Details</h4>
    <ul>
      <li><svg width="20" height="20" viewBox="0 0 20 20" fill="none" stroke="#fff" stroke-width="1.2"><path d="M4 2l3 3-2 2c1 3 3 5 6 6l2-2 3 3-2 3C8 17 3 12 2 4z"/></svg>+1-555-014-2290</li>
      <li><svg width="20" height="20" viewBox="0 0 20 20" fill="none" stroke="#fff" stroke-width="1.2"><rect x="2" y="5" width="16" height="11"/><path d="M2 5l8 6 8-6"/></svg>info@rivetathletic.example</li>
      <li><svg width="20" height="22" viewBox="0 0 20 22" fill="none" stroke="#fff" stroke-width="1.2"><path d="M10 20s6-7 6-11a6 6 0 0 0-12 0c0 4 6 11 6 11z"/><circle cx="10" cy="9" r="2"/></svg>141 Lorem ipsum sit consectetur<br>USA 123456</li>
    </ul>
  </div>
  <div class="foot-rule"></div>
  <div class="copyright">Copyright© 2025 Rivet Athletic - All Right Reserved</div>
</footer>

</body>
</html>
```